Rancho Verbena Wine Bottle Label

Hello! We are looking for a wine bottle label design for our private, family winery located in Chico, CA. The name of our home/ranch/vineyard is Rancho Verbena ('the exit'), which is inspired by our hilltop location, panoramic views of the valley, and sensation of escaping from the busy world below.

We planted our vineyard in 2011 and are now bottling our first harvest from fall of 2013. We planted all Italian varietals on our land: syrah, primitivo, and montepulciano. The wine we make is the culmination of all the love, support and effort poured into the process by our family and friends.

The task at hand: we are looking for a clean, simple front and back wine label design.

Front Label Content:
RV and/or Rancho Verbena
Estate Grown
Chico, CA
Varietal (use Syrah for placeholder)
Year (use 2013 for placeholder)

Back Label Content:
Running list of names of all family and friends who have participated in the process (use a text fill for placeholder)

Aesthetic Description:
Simple, clean, contemporary, text based design (see attached logo idea, Image #1)
Like the brown paper with stamped lettering look & feel
Like the classic clear label with gold lettering look & feel
Option to incorporated a simple background image/sketch of the view overlooking the valley (see attached Image #2 and #3)
Additional inspirational images attached for reference (Images #3- )

General Size Requirement:
Front Label - 4"tall by 3 1/2" wide
Back Label - 4"tall by 3 1/2" wide

Format:
Please submit Photoshop or Illustrator or InDesign Files and PDF/EPS Files.

```html
<!DOCTYPE html>
<html lang="en">
<head>
<meta charset="utf-8">
<title>Rancho Verbena – Syrah Front Label</title>
<link rel="stylesheet" href="https://fonts.googleapis.com/css2?family=Josefin+Sans:wght@300;400;600;700&display=swap">
<style>
  :root {
    --ink: #000000;
    --gold: #fbb93e;
    --rule: #555555;
    --frame: #8a8a8a;
    --paper: #ffffff;
  }
  * { margin: 0; padding: 0; box-sizing: border-box; }
  html, body {
    width: 1200px; height: 900px; overflow: hidden;
    background: var(--paper);
    font-family: "Josefin Sans", sans-serif;
  }
  .canvas { position: relative; width: 1200px; height: 900px; }

  .label {
    position: absolute; left: 346px; top: 102px;
    width: 526px; height: 601px;
    border: 1px solid var(--frame); border-radius: 6px;
    overflow: hidden;
  }
  .monogram {
    position: absolute; left: 0; right: 0; top: 92px;
    text-align: center;
    font-weight: 600; font-size: 190px; line-height: 1;
    color: var(--gold); letter-spacing: -4px;
  }
  .varietal {
    position: absolute; left: 0; right: 0; top: 320px;
    text-align: center;
    font-weight: 600; font-size: 50px; letter-spacing: 3px;
    color: var(--ink);
  }
  .vintage {
    position: absolute; left: 0; right: 0; top: 387px;
    text-align: center;
    font-weight: 300; font-size: 38px; letter-spacing: 2px;
    color: var(--ink);
  }
  .estate-name {
    position: absolute; left: 0; right: 0; top: 531px;
    text-align: center;
    font-weight: 300; font-size: 21px; letter-spacing: 5px;
    color: var(--ink);
  }
  .divider { position: absolute; left: 0; top: 550px; width: 526px; height: 12px; }
  .estate-band {
    position: absolute; left: 0; top: 562px; width: 526px; height: 38px;
  }
  .estate-band .ticks { position: absolute; top: 8px; width: 112px; height: 20px; }
  .estate-band .ticks.left { left: 11px; }
  .estate-band .ticks.right { right: 12px; }
  .estate-band .tag {
    position: absolute; left: 0; right: 0; top: 7px;
    text-align: center;
    font-weight: 700; font-size: 25px; letter-spacing: 3px;
    color: var(--gold);
  }

  .spec { position: absolute; left: 346px; top: 716px; color: var(--ink); }
  .spec .spec-title { font-weight: 600; font-size: 19px; letter-spacing: 0.5px; }
  .spec .spec-size { font-weight: 600; font-size: 18px; letter-spacing: 0.8px; margin-top: 3px; }
  .swatch-list { list-style: none; margin-top: 9px; }
  .swatch-list li {
    display: flex; align-items: center; gap: 13px;
    font-size: 17px; font-weight: 400; height: 24px;
  }
  .swatch-list .chip { width: 20px; height: 20px; }
  .swatch-list .black .chip { background: var(--ink); }
  .swatch-list .gold .chip { background: var(--gold); }
  .swatch-list .gold { color: var(--gold); font-weight: 600; }
</style>
</head>
<body>
<div class="canvas">
  <section class="label">
    <div class="monogram">RV</div>
    <h1 class="varietal">SYRAH</h1>
    <p class="vintage">2013</p>
    <p class="estate-name">RANCHO VERBENA</p>
    <svg class="divider" viewBox="0 0 526 12" aria-hidden="true">
      <line x1="0" y1="6.5" x2="526" y2="6.5" stroke="var(--rule)" stroke-width="1.2"/>
      <path d="M255 7 L262 1 L269 7 Z" fill="var(--ink)"/>
    </svg>
    <div class="estate-band">
      <svg class="ticks left" viewBox="0 0 112 20" aria-hidden="true">
        <g fill="var(--gold)">
          <rect x="0" y="0" width="3" height="20"/><rect x="9.5" y="0" width="3" height="20"/>
          <rect x="19" y="0" width="3" height="20"/><rect x="28.5" y="0" width="3" height="20"/>
          <rect x="38" y="0" width="3" height="20"/><rect x="47.5" y="0" width="3" height="20"/>
          <rect x="57" y="0" width="3" height="20"/><rect x="66.5" y="0" width="3" height="20"/>
          <rect x="76" y="0" width="3" height="20"/><rect x="85.5" y="0" width="3" height="20"/>
          <rect x="95" y="0" width="3" height="20"/><rect x="104.5" y="0" width="3" height="20"/>
        </g>
      </svg>
      <span class="tag">ESTATE GROWN</span>
      <svg class="ticks right" viewBox="0 0 112 20" aria-hidden="true">
        <g fill="var(--gold)">
          <rect x="0" y="0" width="3" height="20"/><rect x="9.5" y="0" width="3" height="20"/>
          <rect x="19" y="0" width="3" height="20"/><rect x="28.5" y="0" width="3" height="20"/>
          <rect x="38" y="0" width="3" height="20"/><rect x="47.5" y="0" width="3" height="20"/>
          <rect x="57" y="0" width="3" height="20"/><rect x="66.5" y="0" width="3" height="20"/>
          <rect x="76" y="0" width="3" height="20"/><rect x="85.5" y="0" width="3" height="20"/>
          <rect x="95" y="0" width="3" height="20"/><rect x="104.5" y="0" width="3" height="20"/>
        </g>
      </svg>
    </div>
  </section>

  <aside class="spec">
    <p class="spec-title">FRONT LABEL</p>
    <p class="spec-size">size - 4x3,5 in</p>
    <ul class="swatch-list">
      <li class="black"><span class="chip"></span>100% Black</li>
      <li class="gold"><span class="chip"></span>gold foil stamping</li>
    </ul>
  </aside>
</div>
</body>
</html>
```